Bramblewood Counselling Group Pty Ltd

clinical psychologist in private practice needs professional stationery package: business cards, complimentary slips, envelopes, range of business letterheads, and logo (photo of lighthouse).

I work with children, adolescents, adults and older population with a range of mental health concerns, adjustment to life transitions and learning difficulties. Majority of my correspondence is with medical practitioners writing reports. I would a clean crisp professional presentation (white background, navy blue text but open to ideas). Thought about having lighthouse as watermark on envelopes. My professional organisation (GTC) logo needs to be on business cards and templates (manual gives guidelines),. The photo of lighthouse is to be included in logo.
There needs to be three letterheads. 1.Is Company only Detail "bramblewood Counselling Group Pty Ltd". 2. Include Company detail and Moira Fensham Clinical Psychologist information at KVRT. 3. Include Company detail and Moira Fensham Clinical Psychologist information at Orchardvale Medical Centre

Target Market(s)

Doctors

Industry/Entity Type

Business

Colors
0355a3
3176b5
0592cd
33a6d7

Requirements
Must have
• Picture of the lighthouse
• GTC logo
• Business name

```html
<!DOCTYPE html>
<html lang="en">
<head>
<meta charset="utf-8">
<title>Stationery Design | Bramblewood Counselling Group</title>
<link href="https://fonts.googleapis.com/css2?family=Bebas+Neue&family=Oswald:wght@500;600&family=Arimo:wght@400&display=swap" rel="stylesheet">
<style>
:root{
  --stage-dark:#1b2540;
  --stage-mid:#2d3d5f;
  --brand-blue:#2f57a8;
  --brand-green:#a6cf3f;
  --paper:#ffffff;
  --faint-blue:#dce2ef;
  --faint-green:#eef5dc;
  --text-blue:#3e5fae;
}
*{margin:0;padding:0;box-sizing:border-box}
html,body{width:1200px;height:1000px;overflow:hidden}
body{position:relative;background:radial-gradient(ellipse at 60% 45%,var(--stage-mid) 0%,var(--stage-dark) 75%);font-family:"Arimo",Arial,sans-serif;color:var(--text-blue)}
.abs{position:absolute}
.hero-badge{left:-120px;top:-25px;width:370px;height:370px;border-radius:50%;background:var(--paper)}
.hero-badge .art{position:absolute;left:22px;top:22px;width:326px;height:326px;border-radius:50%;background:linear-gradient(180deg,var(--brand-blue) 0%,var(--brand-blue) 62%,var(--brand-green) 100%)}
.showcase-title{left:235px;top:38px;font-family:"Bebas Neue",sans-serif;font-weight:400;font-size:35px;color:#fff;letter-spacing:1px;white-space:nowrap}
.showcase-title .divider{display:inline-block;width:3px;height:30px;background:var(--brand-green);margin:0 10px;vertical-align:-3px}
.sheet{background:var(--paper);box-shadow:0 4px 14px rgba(0,0,0,.35);overflow:hidden}
.watermark{position:absolute;border-radius:50%;background:radial-gradient(circle,var(--faint-blue) 0%,var(--faint-blue) 60%,var(--faint-green) 61%,var(--faint-green) 72%,transparent 73%)}
.brand{position:absolute;display:flex;align-items:flex-start;gap:10px}
.brand .dot{border-radius:50%;background:var(--brand-blue);flex:none}
.brand .name{font-family:"Bebas Neue",sans-serif;font-weight:400;color:var(--brand-blue);line-height:.9;text-transform:uppercase;white-space:nowrap}
.brand .name .line2{display:block}
.brand .tagline{font-size:9px;line-height:1.2;color:var(--text-blue);margin-top:4px;white-space:nowrap}
.name-bar{position:absolute;background:var(--brand-blue);color:#fff;font-family:"Oswald",sans-serif;font-weight:500;text-align:right;text-transform:uppercase;white-space:nowrap}
.role-bar{position:absolute;background:var(--brand-green);color:var(--brand-blue);font-family:"Oswald",sans-serif;font-weight:600;text-align:right;text-transform:uppercase;letter-spacing:.5px;white-space:nowrap}
.credentials{position:absolute;text-align:right;line-height:1.28;color:var(--text-blue);white-space:nowrap}
.member{position:absolute;display:flex;align-items:center;gap:6px;color:#333}
.member .seal{border-radius:50%;background:#444;flex:none}
.member .rule{width:1px;background:#666;align-self:stretch}
.stripe{position:absolute}
</style>
</head>
<body>

<div class="abs hero-badge"><div class="art" role="img" aria-label="Brand emblem illustration area in blue and green"></div></div>

<h1 class="abs showcase-title">Stationery Design<span class="divider"></span>Bramblewood Counselling Group</h1>

<!-- Letterhead -->
<section class="abs sheet letterhead" style="left:157px;top:120px;width:583px;height:835px">
  <div class="watermark" role="img" aria-label="Faint brand emblem watermark" style="left:-110px;top:330px;width:440px;height:440px"></div>
  <div class="brand" style="left:23px;top:20px">
    <div class="dot" style="width:66px;height:66px"></div>
    <div>
      <div class="name" style="font-size:44px">Bramblewood<span class="line2" style="font-size:19px">Counselling Group Pty Ltd</span></div>
      <div class="tagline">Navigating life's challenges:<br>learning, wellbeing, relationships and challenge</div>
    </div>
  </div>
  <div class="name-bar" style="left:320px;top:17px;width:263px;height:23px;font-size:18px;line-height:23px;padding-right:20px">Moira Fensham</div>
  <div class="role-bar" style="left:320px;top:40px;width:263px;height:20px;font-size:13px;line-height:20px;padding-right:20px">Clinical Psychologist</div>
  <div class="credentials" style="right:20px;top:64px;font-size:8px">BSc(Psych);BSc(Hons);GradDipEd;MEd;MPsych(Clinical)<br>AHPRA #PSY000481730<br>Medicare Provider # 7302914K &amp; 7302916B<br>Email: Moira.psy@mailhaven.com<br>Therapy and assessment for children, adolescents and adults</div>
  <div class="abs" style="left:23px;top:769px;width:535px;height:1px;background:#9fb0d4"></div>
  <div class="abs" style="left:23px;top:782px;font-size:7.5px;line-height:1.35;color:var(--text-blue)">Clinics: Harlow Street Mental Health, Suite 3, 12 Harlow St, ELMSTEAD, Q4390<br>Clinics: Orchardvale Medical Centre, 27 Penrose St, ORCHARDVALE, Q4318<br>Mail: PO Box 215, KESTON, Q4377<br>Tel: 07 5550 2718, Fax: 07 5550 2719<br>Email: admin@kvrt.com.au, Web: www.kvrt.com.au</div>
  <div class="member" style="left:418px;top:776px;font-size:10px;line-height:1.15">
    <div class="seal" style="width:54px;height:54px"></div><div class="rule"></div>
    <div>Member<br>Guild of<br>Therapy<br>Clinicians MGTC</div>
  </div>
</section>

<!-- Business card -->
<section class="abs sheet card" style="left:843px;top:78px;width:252px;height:154px">
  <div class="watermark" role="img" aria-label="Faint brand emblem watermark" style="left:160px;top:40px;width:120px;height:120px"></div>
  <div class="brand" style="left:108px;top:12px;gap:5px">
    <div class="dot" style="width:30px;height:30px"></div>
    <div class="name" style="font-size:21px">Bramblewood<span class="line2" style="font-size:9px">Counselling Group Pty Ltd</span></div>
  </div>
  <div class="name-bar" style="left:0;top:64px;width:177px;height:15px;font-size:12px;line-height:15px;text-align:left;padding-left:15px">Moira Fensham</div>
  <div class="role-bar" style="left:0;top:79px;width:177px;height:14px;font-size:9px;line-height:14px;text-align:left;padding-left:15px">Clinical Psychologist</div>
  <div class="credentials" style="left:13px;top:99px;text-align:left;font-size:5.5px">BSc(Psych);BSc(Hons);GradDipEd;MEd;MPsych(Clinical)<br>AHPRA #PSY000481730<br>Medicare Provider # 7302914K &amp; 7302916B<br>Email: Moira.psy@mailhaven.com<br>Therapy and assessment for children, adolescents and adults</div>
  <div class="member" style="left:178px;top:114px;font-size:5px;line-height:1.1;gap:3px">
    <div class="seal" style="width:16px;height:16px"></div>
    <div>Member<br>Guild of Therapy<br>Clinicians MGTC</div>
  </div>
  <div class="stripe" style="left:0;top:147px;width:252px;height:4px;background:var(--brand-green)"></div>
  <div class="stripe" style="left:125px;top:146px;width:127px;height:8px;background:var(--brand-blue)"></div>
</section>

<!-- Compliment slip -->
<section class="abs sheet slip" style="left:503px;top:265px;width:602px;height:248px">
  <div class="watermark" role="img" aria-label="Faint brand emblem watermark" style="left:5px;top:20px;width:285px;height:285px"></div>
  <div class="brand" style="left:15px;top:25px">
    <div class="dot" style="width:72px;height:72px"></div>
    <div>
      <div class="name" style="font-size:44px">Bramblewood<span class="line2" style="font-size:19px">Counselling Group Pty Ltd</span></div>
      <div class="tagline" style="font-size:8px">Navigating life's challenges:<br>learning, wellbeing, relationships and challenge</div>
    </div>
  </div>
  <div class="name-bar" style="left:350px;top:32px;width:252px;height:21px;font-size:14px;line-height:21px;text-align:center;letter-spacing:4px">Compliment Slip</div>
  <div class="stripe" style="left:350px;top:53px;width:252px;height:19px;background:var(--brand-green)"></div>
</section>

<!-- DL letterhead -->
<section class="abs sheet dl-letterhead" style="left:502px;top:538px;width:601px;height:300px">
  <div class="brand" style="left:23px;top:18px">
    <div class="dot" style="width:76px;height:76px"></div>
    <div>
      <div class="name" style="font-size:44px">Bramblewood<span class="line2" style="font-size:19px">Counselling Group Pty Ltd</span></div>
      <div class="tagline" style="font-size:8px">Navigating life's challenges:<br>learning, wellbeing, relationships and challenge</div>
    </div>
  </div>
  <div class="name-bar" style="left:349px;top:25px;width:252px;height:22px;font-size:17px;line-height:22px;padding-right:20px">Moira Fensham</div>
  <div class="role-bar" style="left:349px;top:47px;width:252px;height:18px;font-size:12px;line-height:18px;padding-right:20px">Clinical Psychologist</div>
  <div class="credentials" style="right:20px;top:69px;font-size:7.5px">BSc(Psych);BSc(Hons);GradDipEd;MEd;MPsych(Clinical)<br>AHPRA #PSY000481730<br>Medicare Provider # 7302914K &amp; 7302916B<br>Email: Moira.psy@mailhaven.com<br>Therapy and assessment for children, adolescents and adults</div>
  <div class="stripe" style="left:0;top:273px;width:601px;height:14px;background:var(--brand-blue)"></div>
  <div class="stripe" style="left:0;top:287px;width:601px;height:13px;background:var(--brand-green)"></div>
</section>

</body>
</html>
```